Plakat-Design für Garten- und Landschaftsbau
Zielgruppe
Unsere Firma beschäftigt sich mit dem Garten- und Landschaftsbau, das heißt wie gestalten Gärten neu, führen Baggerarbeiten und Erdarbeiten durch.
Und sind in dem Forst und Rodungsarbeiten aktiv
Aufgabenstellung
Dies soll ein Banner sein das an Bauzäune angebracht wird Format bzw. Verhältnis sollte bxh 2:1 sein
Der Banner soll mit einen oder meheren Bildern versehen werden im Hintergrund oder im Vordergrund.

```html
<!DOCTYPE html>
<html lang="de">
<head>
<meta charset="utf-8">
<title>Holtwerk Gartenbau – Bauzaunbanner</title>
<link href="https://fonts.googleapis.com/css2?family=Open+Sans:wght@400;600;700&display=swap" rel="stylesheet">
<style>
  :root {
    --page: #ececec;
    --brand-green: #4a9440;
    --brand-green-dark: #2f6e2c;
    --ink: #4a4a4a;
    --paper: #ffffff;
    --bark-dark: #2a2c27;
    --bark-mid: #4f534a;
    --ivy: #2f4a2a;
    --moss-dark: #0f1f10;
    --moss-mid: #2c4a2a;
  }
  * { margin: 0; padding: 0; box-sizing: border-box; }
  html, body { width: 1200px; height: 1198px; overflow: hidden; }
  body {
    position: relative;
    background: var(--page);
    font-family: "Open Sans", Arial, sans-serif;
  }
  .brand-header {
    position: absolute;
    left: 96px; top: 110px;
    display: flex; align-items: center; gap: 12px;
    color: var(--brand-green-dark);
    font-weight: 700;
    font-size: 34px;
    letter-spacing: 0.5px;
  }
  .brand-mark {
    width: 26px; height: 26px;
    background: var(--brand-green);
    flex: none;
  }
  .banner {
    position: absolute;
    left: 303px;
    width: 777px; height: 388px;
    background: var(--paper);
    overflow: hidden;
  }
  .banner--bark { top: 274px; }
  .banner--tools { top: 728px; }
  .banner__art {
    position: absolute; inset: 0;
    width: 777px; height: 388px;
  }
  .services {
    position: absolute;
    left: 43px; top: 93px;
    color: #fff;
    font-size: 16px;
    line-height: 22.5px;
    letter-spacing: 1.3px;
    font-weight: 700;
    text-transform: uppercase;
    list-style: none;
  }
  .services--extra {
    top: 227px;
    font-weight: 400;
  }
  .services--extra .services__title { font-weight: 700; }
  .banner__brand {
    position: absolute;
    left: 486px; top: 102px;
    width: 264px;
    display: flex; align-items: center; gap: 9px;
    color: var(--brand-green-dark);
    font-weight: 700;
    font-size: 22px;
    line-height: 30px;
  }
  .banner__brand .brand-mark { width: 18px; height: 18px; }
  .contact {
    position: absolute;
    right: 27px; top: 280px;
    text-align: right;
    color: var(--ink);
    font-weight: 600;
    font-size: 14.5px;
    line-height: 22px;
    letter-spacing: 0.3px;
  }
</style>
</head>
<body>

  <div class="brand-header"><span class="brand-mark"></span>Holtwerk Gartenbau GmbH</div>

  <section class="banner banner--bark">
    <svg class="banner__art" viewBox="0 0 777 388" preserveAspectRatio="none">
      <defs>
        <linearGradient id="bark" x1="0" y1="0" x2="1" y2="0.4">
          <stop offset="0" stop-color="var(--bark-mid)"/>
          <stop offset="0.5" stop-color="var(--bark-dark)"/>
          <stop offset="1" stop-color="var(--ivy)"/>
        </linearGradient>
      </defs>
      <polygon role="img" aria-label="Foto: Baumrinde mit Efeuranken" fill="url(#bark)" points="0,0 485,0 352,388 0,388"/>
      <polygon fill="var(--brand-green)" points="485,0 379,388 352,388"/>
    </svg>
    <ul class="services">
      <li>- Garten-und Landschaftsbau</li>
      <li>- Baggerbetrieb</li>
      <li>- Erdbau</li>
      <li>- Gebäudemanagement</li>
      <li>- Forst-und Rodungsarbeiten</li>
    </ul>
    <ul class="services services--extra">
      <li class="services__title">Individuelle Gartengestaltung</li>
      <li>- Terassenbau</li>
      <li>- Plasterarbeiten</li>
    </ul>
    <div class="banner__brand"><span class="brand-mark"></span><span>Holtwerk Gartenbau<br>GmbH</span></div>
    <div class="contact">
      <p>Telefon 0176/2384519</p>
      <p>info@holtwerk-gartenbau-test.de</p>
      <p>www.holtwerk-gartenbau-test.de</p>
    </div>
  </section>

  <section class="banner banner--tools">
    <svg class="banner__art" viewBox="0 0 777 388" preserveAspectRatio="none">
      <defs>
        <linearGradient id="moss" x1="0" y1="0" x2="0.8" y2="1">
          <stop offset="0" stop-color="var(--moss-mid)"/>
          <stop offset="0.55" stop-color="var(--moss-dark)"/>
          <stop offset="1" stop-color="#1c331b"/>
        </linearGradient>
      </defs>
      <polygon role="img" aria-label="Foto: Gartenschaufel mit Erde auf Holzbrettern, grün eingefärbt" fill="url(#moss)" points="0,0 485,0 352,388 0,388"/>
      <polygon fill="var(--brand-green)" points="485,0 379,388 352,388"/>
    </svg>
    <ul class="services">
      <li>- Garten-und Landschaftsbau</li>
      <li>- Baggerbetrieb</li>
      <li>- Erdbau</li>
      <li>- Gebäudemanagement</li>
      <li>- Forst-und Rodungsarbeiten</li>
    </ul>
    <ul class="services services--extra">
      <li class="services__title">Individuelle Gartengestaltung</li>
      <li>- Terassenbau</li>
      <li>- Plasterarbeiten</li>
    </ul>
    <div class="banner__brand"><span class="brand-mark"></span><span>Holtwerk Gartenbau<br>GmbH</span></div>
    <div class="contact">
      <p>Telefon 0176/2384519</p>
      <p>info@holtwerk-gartenbau-test.de</p>
      <p>www.holtwerk-gartenbau-test.de</p>
    </div>
  </section>

</body>
</html>
```